IV Nutritional Clinic Web Design

We are working with Velmo. They are an IV Nutritional Clinic and in need of a new website design.
Some sites to use for inspiration:
https://brantlowcare.example
https://www.zolvarihealth.example
https://www.quellspa.example
https://pimrolift.example
https://www.dorvak-well.example/pages/iv-therapy-west-hollywood
https://www.tqoncowell.example/cancer-care/iv-drips/
https://drelmavita.example
https://salbrikmed.example
Thank you for taking the time to consider designing a website for us. We are web developers based in Stockton, CA, USA. Most of our projects go through the same process. Understanding this process may help you win a project with us. We custom-code all of our websites in-house. We don’t have any requirements as to what tools you use for your design, but we prefer Figma files. For any design that we label as four-stars, we send it to the client for review. The client picks the final design they want us to use. Once we complete this process, we will continue to show additional clients all the four-star sites and purchase them later. Your designs will have multiple chances to sell. For better chances of success, we ask that you follow these guidelines.
IMAGES:
If you use any images or icons in the design, we ask that you have a link to the asset so we can purchase the image/icon. Most of the designs we submit do not have the customer’s images on them unless they have some great images. Be creative; show us the feeling you are trying to portray with your image choices. Use any royalty-free site you choose. We subscribe to Corvix and mainly use their images, but we can purchase images outside of Corvix.
PLEASE NOTE: we will not submit designs to clients with watermarks on the images.
FONTS:
We ask that you identify the fonts used in the design. This can be done in a message if you want. We typically use Lumen Typeset and Corvix Fonts.
CONTENT:
We're always open to different content and ideas. We often submit designs with stock images so the client can see our vision. We typically take pictures after the website launch to use their images with our vision. Lorem Ipsum is fine for paragraphs, but we ask that you write the headers in correct English. We want to be able to show the vision and identify the sections of the website.
INSPIRATION:
We typically add a couple of links in the brief of websites we like to help you get started in your design.
REVISIONS:
We do not often ask for revisions of the designs unless we see something in the design that may not appeal to the client. If there are slight changes that we want to make, we do that in the development process.
FEEDBACK:
We rarely give feedback on designs during the design process. We are working on many website projects and do not have the time to provide feedback. We usually respond if your request is well thought out and asks specific questions, but a note asking “feedback, please” usually goes unanswered.
Number of Pages Required
1 page
Look and feel
Each slider illustrates characteristics of the customer's brand and the style your logo design should communicate.

```html
<!DOCTYPE html>
<html lang="en">
<head>
<meta charset="utf-8">
<title>Velmo – IV Nutritional Therapy</title>
<link href="https://fonts.googleapis.com/css2?family=Montserrat:wght@500;600;700;800&family=Jost:wght@400;500;600&display=swap" rel="stylesheet">
<style>
:root{
  --navy:#1c1f78;
  --navy-deep:#141a6e;
  --green:#6b9a35;
  --green-dark:#4f7f22;
  --text:#4a4a55;
  --muted:#777a86;
  --soft:#eef0f6;
  --white:#ffffff;
  --line:#e3e5ec;
}
*{margin:0;padding:0;box-sizing:border-box}
html,body{width:1200px;height:4666px;overflow:hidden}
body{position:relative;background:var(--white);font-family:"Jost",sans-serif;color:var(--text)}
.abs{position:absolute}
.center{left:0;width:1200px;text-align:center}
h1,h2,h3{font-family:"Montserrat",sans-serif;color:var(--navy)}
.section-title{font-size:31px;font-weight:600;letter-spacing:.3px}
.section-sub{font-size:14px;color:var(--muted)}
.lead{font-size:14px;line-height:33px;color:var(--muted)}
.btn{display:flex;align-items:center;justify-content:center;background:var(--green);color:var(--white);font-size:15px;font-weight:500}
.btn.navy{background:var(--navy)}
.social{display:flex;gap:14px}
.social span{width:36px;height:36px;background:var(--white);box-shadow:0 4px 12px rgba(0,0,0,.12);display:block}
.social span:first-child{background:var(--navy)}
.brand{font-family:"Montserrat",sans-serif;font-weight:800;color:var(--navy);letter-spacing:2px;display:flex;align-items:center;gap:12px}
.brand i{display:block;background:var(--green)}
/* header */
.topline{top:0;left:0;width:1200px;height:4px;background:var(--green)}
.nav a{position:absolute;top:112px;font-size:19px;color:var(--text);text-decoration:none}
.nav a.active{color:var(--green)}
.call{top:42px;left:866px;display:flex;gap:16px;align-items:center}
.call .ico{width:38px;height:38px;background:var(--navy);display:flex;align-items:center;justify-content:center}
.call small{display:block;font-size:9px;color:var(--text)}
.call strong{font-family:"Montserrat",sans-serif;font-size:20px;color:var(--navy);font-weight:700}
/* hero */
.hero{top:160px;left:0;width:1200px;height:570px;background:linear-gradient(90deg,#c9ccd2 0%,#dcdee2 45%,#e9eaec 62%,#cfd2d6 100%)}
.hero h1{position:absolute;left:110px;top:95px;font-size:64px;line-height:78px;font-weight:700;letter-spacing:1px}
.hero .band{position:absolute;left:110px;top:260px;width:488px;height:68px;background:var(--green);color:var(--white);font-family:"Montserrat",sans-serif;font-weight:600;font-size:26px;display:flex;align-items:center;padding-left:16px}
.hero p{position:absolute;left:110px;top:352px;width:500px;font-size:21px;line-height:35px;color:#2f2f3a}
.dots-v{position:absolute;left:1133px;top:240px;display:flex;flex-direction:column;gap:7px}
.dots-v span{width:9px;height:9px;border:1px solid var(--navy)}
.dots-v span:first-child{background:var(--navy)}
/* features */
.feature{position:absolute;top:980px;width:188px;height:188px;background:var(--white);box-shadow:0 6px 22px rgba(28,31,120,.1);text-align:center;font-size:13.5px;line-height:22px;color:var(--text)}
.feature .ic{width:56px;height:56px;border-radius:50%;background:var(--green);margin:30px auto 12px;display:flex;align-items:center;justify-content:center}
.feature.on{background:var(--green);color:var(--white)}
.feature.on .ic{background:var(--white)}
/* services */
.services-bg{top:1397px;left:0;width:1200px;height:663px;background:var(--soft)}
.service{position:absolute;top:1558px;width:236px;text-align:center}
.service .photo{height:304px;position:relative;border:3px solid var(--white)}
.service .go{position:absolute;right:14px;bottom:14px;width:30px;height:30px;border-radius:50%;background:var(--navy);display:flex;align-items:center;justify-content:center}
.service.alt .go{background:var(--green)}
.service h3{font-family:"Jost",sans-serif;font-size:17px;font-weight:500;color:#222;margin-top:20px}
.service.alt h3{color:var(--green)}
.service p{font-size:12.5px;line-height:23px;color:var(--muted);margin-top:6px}
.price{margin-top:8px;font-family:"Montserrat",sans-serif;font-weight:700;font-size:21px;color:var(--navy)}
.service.alt .price{color:var(--green)}
.price s{font-size:10px;color:var(--muted);font-weight:500;margin-left:8px;text-decoration:none}
/* how it works */
.green-band{top:2657px;left:0;width:1200px;height:801px;background:linear-gradient(135deg,#4f8a1f 0%,#6c9e36 45%,#5a8f2a 100%)}
.video{top:2450px;left:205px;width:790px;height:413px;border:4px solid var(--white);background:linear-gradient(90deg,#dedede,#f1f1f1 50%,#d9d9d9)}
.play{position:absolute;left:365px;top:176px;width:54px;height:54px;border-radius:50%;background:var(--navy);display:flex;align-items:center;justify-content:center;box-shadow:0 0 0 14px rgba(28,31,120,.25)}
.step{position:absolute;top:3013px;width:270px;height:357px;background:var(--white);padding:22px 22px 0}
.step .num{display:flex;gap:20px;align-items:center}
.step .num b{font-family:"Montserrat",sans-serif;font-size:44px;color:var(--navy);font-weight:600}
.step.alt .num b{color:var(--green)}
.step .num span{font-size:14px;line-height:21px;color:var(--muted)}
.step p{margin-top:22px;font-size:12.5px;line-height:26.5px;color:var(--muted);text-align:justify;text-align-last:center}
.step .btn{width:128px;height:36px;margin:18px auto 0;font-size:13px}
/* testimonials */
.quote{position:absolute;top:3617px;width:446px;height:308px;background:var(--white);border:1px solid var(--line);box-shadow:0 6px 22px rgba(0,0,0,.05);text-align:center;padding:34px 26px 0;font-size:13px;line-height:29px;color:var(--muted)}
.quote cite{display:block;margin-top:12px;font-style:normal;color:var(--green);font-size:15px;line-height:20px}
.stars{display:flex;justify-content:center;gap:2px}
.dots-h{top:3951px;left:570px;display:flex;gap:7px}
.dots-h span{width:9px;height:9px;border:1px solid var(--navy)}
.dots-h span:first-child{background:var(--navy)}
/* newsletter */
.news{top:4005px;left:0;width:1200px;height:325px;background:linear-gradient(120deg,#1a2a9a 0%,#1e2f9d 40%,#152385 100%)}
.news h2{color:var(--white)}
.field{position:absolute;top:4187px;width:272px;height:46px;background:var(--white);display:flex;align-items:center;justify-content:space-between;padding:0 20px;font-size:13px;color:#555}
/* footer */
.foot h4{position:absolute;top:4386px;font-family:"Montserrat",sans-serif;font-size:19px;color:var(--navy);font-weight:700}
.foot ul{position:absolute;top:4428px;list-style:none}
.foot li{display:flex;align-items:center;gap:14px;height:30px;font-size:14px;color:var(--text)}
.foot li .dot{width:12px;height:12px;border-radius:50%;background:var(--green);flex:none}
.divider{top:4603px;left:110px;width:980px;height:1px;background:var(--line)}
</style>
</head>
<body>

<!-- Header -->
<div class="abs topline"></div>
<div class="abs social" style="top:43px;left:112px"><span></span><span></span><span></span><span></span></div>
<div class="abs brand" style="top:36px;left:472px;font-size:66px"><i style="width:16px;height:16px"></i>VELMO</div>
<div class="abs call">
  <div class="ico"><svg width="16" height="16" viewBox="0 0 24 24"><path fill="#fff" d="M6.6 10.8a15.1 15.1 0 0 0 6.6 6.6l2.2-2.2a1 1 0 0 1 1-.25 11.4 11.4 0 0 0 3.6.57 1 1 0 0 1 1 1V20a1 1 0 0 1-1 1A17 17 0 0 1 3 4a1 1 0 0 1 1-1h3.5a1 1 0 0 1 1 1c0 1.25.2 2.45.57 3.57a1 1 0 0 1-.25 1z"/></svg></div>
  <div><small>Call Us:</small><strong>+1 555 010 0199</strong></div>
</div>
<nav class="nav">
  <a class="active" style="left:110px">Home</a>
  <a style="left:205px">About Us</a>
  <a style="left:330px">Services</a>
  <a style="left:795px">Reviews</a>
  <a style="left:910px">Blog</a>
  <a style="left:992px">Contact Us</a>
</nav>

<!-- Hero -->
<section class="abs hero" role="img" aria-label="Woman relaxing in a white robe in a recliner during an IV drip session, holding a glass">
  <h1>REVITALIZE<br>YOUR HEALTH</h1>
  <div class="band">WITH IV NUTRITIONAL THERAPY</div>
  <p>We offer a peaceful, comfortable setting designed to make your wellness journey as enjoyable as possible.</p>
  <div class="dots-v"><span></span><span></span><span></span><span></span><span></span></div>
</section>

<!-- Intro -->
<h2 class="abs center section-title" style="top:792px">NOURISHMENT THAT GOES BEYOND THE SURFACE</h2>
<p class="abs lead" style="top:850px;left:190px;width:820px;text-align:center">Sed ut perspiciatis unde omnis iste natus error sit voluptatem accusantium doloremque laudantium, totam rem aperiam, eaque ipsa quae ab illo inventore veritatis et quasi architecto beatae vitae dicta sunt explicabo. Nemo enim ipsam voluptatem quia voluptas sit aspernatur aut odit aut fugit</p>

<div class="feature" style="left:293px">
  <div class="ic"><svg width="26" height="26" viewBox="0 0 24 24"><path d="M9 3h6v4l-1 1v5a2 2 0 0 1-4 0V8L9 7z" fill="none" stroke="#fff" stroke-width="2"/><path d="M12 15v6" stroke="#fff" stroke-width="2"/></svg></div>
  Personalized<br>Treatments for Every<br>Need
</div>
<div class="feature on" style="left:505px">
  <div class="ic"><svg width="26" height="26" viewBox="0 0 24 24"><circle cx="12" cy="7" r="3" fill="#6b9a35"/><path d="M5 19c1-4 4-6 7-6s6 2 7 6z" fill="#6b9a35"/></svg></div>
  Effective<br>&amp; Comprehensive<br>Wellness Approach
</div>
<div class="feature" style="left:718px">
  <div class="ic"><svg width="28" height="28" viewBox="0 0 24 24"><circle cx="12" cy="12" r="8" fill="none" stroke="#fff" stroke-width="2"/><path d="M8 12l3 3 5-6" fill="none" stroke="#fff" stroke-width="2"/></svg></div>
  Certified<br>And Experienced<br>Professionals
</div>

<p class="abs lead" style="top:1205px;left:180px;width:840px;text-align:center">Ut enim ad minima veniam, quis nostrum exercitationem ullam corporis suscipit laboriosam, nisi ut aliquid ex ea commodi consequatur? Quis autem vel eum iure reprehenderit qui in ea voluptate</p>
<div class="abs btn" style="top:1290px;left:514px;width:172px;height:46px">Explore More</div>

<!-- Services -->
<div class="abs services-bg"></div>
<h2 class="abs center section-title" style="top:1462px">SERVICES OFFERED</h2>
<p class="abs center section-sub" style="top:1507px">Quis autem vel eum iure reprehenderit qui in ea voluptate velit esse quam nihil</p>

<div class="service" style="left:98px">
  <div class="photo" role="img" aria-label="Clinician preparing a relaxed patient for a hydration drip" style="background:linear-gradient(160deg,#9fb6c4,#e7ecef 60%,#cfd6dc)"><span class="go"><svg width="12" height="12" viewBox="0 0 12 12"><path d="M3 9l6-6M4 3h5v5" fill="none" stroke="#fff" stroke-width="1.5"/></svg></span></div>
  <h3>Hydration Therapy</h3>
  <p>Quis autem vel eum iure reprehen<br>derit qui in ea voluptate</p>
  <div class="price">$340<s>$450</s></div>
</div>
<div class="service alt" style="left:355px">
  <div class="photo" role="img" aria-label="Woman holding an orange vitamin infusion bag" style="background:linear-gradient(160deg,#4a2a1c,#9a5a30 50%,#e0a030)"><span class="go"><svg width="12" height="12" viewBox="0 0 12 12"><path d="M3 9l6-6M4 3h5v5" fill="none" stroke="#fff" stroke-width="1.5"/></svg></span></div>
  <h3>Vitamin Infusions</h3>
  <p>Quis autem vel eum iure reprehen<br>derit qui in ea voluptate</p>
  <div class="price">$340<s>$450</s></div>
</div>
<div class="service" style="left:611px">
  <div class="photo" role="img" aria-label="Nurse giving an immune booster drip to a smiling patient" style="background:linear-gradient(160deg,#b9c6d3,#eef0f2 55%,#c9d1da)"><span class="go"><svg width="12" height="12" viewBox="0 0 12 12"><path d="M3 9l6-6M4 3h5v5" fill="none" stroke="#fff" stroke-width="1.5"/></svg></span></div>
  <h3>Immune Boosters</h3>
  <p>Quis autem vel eum iure reprehen<br>derit qui in ea voluptate</p>
  <div class="price">$340<s>$450</s></div>
</div>
<div class="service" style="left:867px">
  <div class="photo" role="img" aria-label="Doctor administering an IV injection to a seated patient" style="background:linear-gradient(160deg,#e6e8ec,#c7ccd6 55%,#8f9db8)"><span class="go"><svg width="12" height="12" viewBox="0 0 12 12"><path d="M3 9l6-6M4 3h5v5" fill="none" stroke="#fff" stroke-width="1.5"/></svg></span></div>
  <h3>IV Injection</h3>
  <p>Quis autem vel eum iure reprehen<br>derit qui in ea voluptate</p>
  <div class="price">$340<s>$450</s></div>
</div>

<!-- About -->
<h2 class="abs center section-title" style="top:2107px">ABOUT VELMO</h2>
<p class="abs lead" style="top:2157px;left:190px;width:820px;text-align:center">Sed ut perspiciatis unde omnis iste natus error sit voluptatem accusantium doloremque laudantium, totam rem aperiam, eaque ipsa quae ab illo inventore veritatis et quasi architecto beatae vitae dicta sunt explicabo. Nemo enim ipsam voluptatem quia voluptas sit aspernatur aut odit aut fugit</p>
<p class="abs lead" style="top:2264px;left:180px;width:840px;text-align:center">Ut enim ad minima veniam, quis nostrum exercitationem ullam corporis suscipit laboriosam, nisi ut aliquid ex ea commodi consequatur? Quis autem vel eum iure reprehenderit qui in ea voluptate</p>
<div class="abs btn" style="top:2356px;left:514px;width:172px;height:46px">Explore More</div>

<!-- How it works -->
<div class="abs green-band" role="img" aria-label="Green-tinted backdrop of IV drip equipment"></div>
<div class="abs video" role="img" aria-label="Video still of two clients in white robes relaxing in armchairs during IV therapy">
  <div class="play"><svg width="16" height="16" viewBox="0 0 16 16"><path d="M4 2l10 6-10 6z" fill="#fff"/></svg></div>
</div>
<h2 class="abs center section-title" style="top:2925px;color:#fff">HOW IV THERAPY WORKS</h2>
<p class="abs center section-sub" style="top:2970px;color:#eef4e6">Quis autem vel eum iure reprehenderit qui in ea voluptate velit esse quam nihil</p>

<div class="step" style="left:167px">
  <div class="num"><b>01</b><span>Consultation and<br>Customization</span></div>
  <p>Neque porro quisquam est, qui dolorem ipsum quia dolor sit amet, consectetur, adipisci velit, sed quia non numquam eius modi tempora incidunt ut labore et dolore magnam aliquam quaerat voluptatem. Ut enim ad minima veniam,</p>
  <div class="btn navy">Explore More</div>
</div>
<div class="step alt" style="left:465px">
  <div class="num"><b>02</b><span>IV Drip<br>Administration</span></div>
  <p>Neque porro quisquam est, qui dolorem ipsum quia dolor sit amet, consectetur, adipisci velit, sed quia non numquam eius modi tempora incidunt ut labore et dolore magnam aliquam quaerat voluptatem. Ut enim ad minima veniam,</p>
  <div class="btn">Explore More</div>
</div>
<div class="step" style="left:763px">
  <div class="num"><b>03</b><span>Relaxation &amp;<br>Replenishment</span></div>
  <p>Neque porro quisquam est, qui dolorem ipsum quia dolor sit amet, consectetur, adipisci velit, sed quia non numquam eius modi tempora incidunt ut labore et dolore magnam aliquam quaerat voluptatem. Ut enim ad minima veniam,</p>
  <div class="btn navy">Explore More</div>
</div>

<!-- Testimonials -->
<h2 class="abs center section-title" style="top:3521px">OUR HAPPY CUSTOMERS</h2>
<p class="abs center section-sub" style="top:3568px">Quis autem vel eum iure reprehenderit qui in ea voluptate velit esse quam nihil</p>
<svg class="abs" style="top:3585px;left:120px" width="52" height="42" viewBox="0 0 52 42"><path d="M0 42V22C0 9 7 2 20 0v8c-6 2-9 6-9 12h9v22zM30 42V22C30 9 37 2 50 0v8c-6 2-9 6-9 12h9v22z" fill="#1c1f78"/></svg>

<div class="quote" style="left:147px">
  Neque porro quisquam est, qui dolorem ipsum quia dolor sit amet, consectetur, adipisci velit, sed quia non numquam eius modi tempora incidunt ut labore et dolore magnam aliquam quaerat voluptatem. Ut enim ad minima veniam, quis nostrum exercitationem ullam corporis suscipit laboriosam, nisi ut aliquid ex ea
  <cite>- Rina Castell</cite>
  <div class="stars"><svg width="60" height="10" viewBox="0 0 60 10"><g fill="#e0a020"><path id="st" d="M5 0l1.5 3.3 3.5.4-2.6 2.4.7 3.5L5 7.8 1.9 9.6l.7-3.5L0 3.7l3.5-.4z"/><use href="#st" x="12"/><use href="#st" x="24"/><use href="#st" x="36"/><use href="#st" x="48"/></g></svg></div>
</div>
<div class="quote" style="left:631px">
  Neque porro quisquam est, qui dolorem ipsum quia dolor sit amet, consectetur, adipisci velit, sed quia non numquam eius modi tempora incidunt ut labore et dolore magnam aliquam quaerat voluptatem. Ut enim ad minima veniam, quis nostrum exercitationem ullam corporis suscipit laboriosam, nisi ut aliquid ex ea
  <cite>- Rina Castell</cite>
  <div class="stars"><svg width="60" height="10" viewBox="0 0 60 10"><g fill="#e0a020"><use href="#st"/><use href="#st" x="12"/><use href="#st" x="24"/><use href="#st" x="36"/><use href="#st" x="48"/></g></svg></div>
</div>
<div class="abs dots-h"><span></span><span></span><span></span><span></span></div>

<!-- Newsletter -->
<section class="abs news" role="img" aria-label="Blue-tinted backdrop of a nurse setting up an IV line"></section>
<h2 class="abs center section-title" style="top:4088px;color:#fff">SUBSCRIBE TO JOIN OUR NEWSLETTER</h2>
<p class="abs center section-sub" style="top:4133px;color:#dfe3ff">Quis autem vel eum iure reprehenderit qui in ea voluptate velit esse quam nihil</p>
<div class="field" style="left:206px">Full Name<svg width="12" height="12" viewBox="0 0 12 12"><circle cx="6" cy="3.5" r="2.5" fill="#555"/><path d="M1 12c0-3 2-5 5-5s5 2 5 5z" fill="#555"/></svg></div>
<div class="field" style="left:500px">Email Address<svg width="14" height="10" viewBox="0 0 14 10"><rect width="14" height="10" fill="#555"/><path d="M0 0l7 5 7-5" fill="none" stroke="#fff" stroke-width="1.2"/></svg></div>
<div class="abs btn" style="top:4187px;left:795px;width:198px;height:46px;font-size:14px">Subscribe Now</div>

<!-- Footer -->
<footer class="foot">
  <div class="abs brand" style="top:4390px;left:112px;font-size:60px"><i style="width:14px;height:14px"></i>VELMO</div>
  <div class="abs social" style="top:4518px;left:112px"><span></span><span></span><span></span><span></span></div>

  <h4 style="left:439px">QUICK LINKS</h4>
  <ul style="left:439px">
    <li><span class="dot"></span>Home</li><li><span class="dot"></span>About Us</li><li><span class="dot"></span>Services</li><li><span class="dot"></span>Reviews</li><li><span class="dot"></span>Contact Us</li>
  </ul>
  <h4 style="left:640px">HELP LINKS</h4>
  <ul style="left:640px">
    <li><span class="dot"></span>Help</li><li><span class="dot"></span>Sitemap</li><li><span class="dot"></span>Privacy Policy</li><li><span class="dot"></span>Terms Of Use</li>
  </ul>
  <h4 style="left:831px">CONTACT US</h4>
  <ul style="left:831px;width:270px">
    <li style="height:54px;align-items:flex-start;line-height:27px"><svg width="12" height="14" viewBox="0 0 12 14" style="margin-top:6px;flex:none"><path d="M6 0a5 5 0 0 1 5 5c0 4-5 9-5 9S1 9 1 5a5 5 0 0 1 5-5z" fill="#6b9a35"/><circle cx="6" cy="5" r="2" fill="#fff"/></svg>Velmo, eum iure reprehenderit qui in United States</li>
    <li><svg width="12" height="12" viewBox="0 0 24 24" style="flex:none"><path fill="#6b9a35" d="M6.6 10.8a15.1 15.1 0 0 0 6.6 6.6l2.2-2.2a1 1 0 0 1 1-.25 11.4 11.4 0 0 0 3.6.57 1 1 0 0 1 1 1V20a1 1 0 0 1-1 1A17 17 0 0 1 3 4a1 1 0 0 1 1-1h3.5a1 1 0 0 1 1 1c0 1.25.2 2.45.57 3.57a1 1 0 0 1-.25 1z"/></svg>Phone: +1 555 010 (0199)</li>
    <li><svg width="13" height="10" viewBox="0 0 14 10" style="flex:none"><rect width="14" height="10" fill="#6b9a35"/><path d="M0 0l7 5 7-5" fill="none" stroke="#fff" stroke-width="1.2"/></svg>Email: info@velmo.example</li>
  </ul>
  <div class="abs divider"></div>
  <p class="abs center" style="top:4628px;font-size:13px;color:var(--text)">(C) Copyright | All Rights Reserved</p>
</footer>

</body>
</html>
```